Talvera Web site

Talvera is a trade name for Dresgan enterprises llc, would like Dresgan mentioned but not prominent.

Use current logo to base colors and look/feel of website. Modern trendy look.

Talvera Technical Services - "Irrevocably committed to your success"

Website design for a nation wide service based company

Networking, AV, access control, automation, EAS, project management, consulting, electrical, design, service staffing

Hostwick hosts our URL's

Questions-
Who owns the content once accepted.
How is the content delivered to build site
How do we adjust. or add to content once published

Target Market(s)

commercial and retail technical services. IE, we provide technical services for retail and commercial vertical markets

Industry/Entity Type

Trade

Coding

Coded - Design and coding required

Number of Pages Required

5+ page

Font styles to use
Sans Serif

Colors
3276b5

Requirements
Must have
• Pages-
• About/info, contact, services, customers log in portal, social media links
• links to outside web based software portals
• Call through (call me) links

```html
<!DOCTYPE html>
<html lang="en">
<head>
<meta charset="utf-8">
<title>Talvera Technical Services</title>
<link rel="stylesheet" href="https://fonts.googleapis.com/css2?family=Open+Sans:wght@400;600;700&display=swap">
<style>
:root{
  --brand:#3276b5;
  --brand-dark:#1d4f8c;
  --sky:#119ee0;
  --ink:#2b2b2b;
  --text:#666;
  --muted:#8a8a8a;
  --line:#e3e3e3;
  --panel:#ededed;
  --charcoal:#2f3133;
  --footer-bar:#2a2c2e;
  --white:#fff;
}
*{box-sizing:border-box;margin:0;padding:0}
html,body{width:1200px;height:2323px;overflow:hidden}
body{position:relative;background:var(--white);font-family:"Open Sans",sans-serif;color:var(--text)}
a{color:inherit;text-decoration:none}
.abs{position:absolute}

/* header */
.topline{left:0;top:0;width:1200px;height:4px;background:var(--charcoal)}
.brand{left:165px;top:14px;display:flex;align-items:center;gap:10px}
.brand-mark{width:34px;height:34px;border-radius:50%;background:var(--brand);flex:none}
.brand-text{display:flex;flex-direction:column;line-height:1}
.brand-name{font-size:26px;font-weight:700;color:var(--brand-dark);letter-spacing:.5px}
.brand-tagline{font-size:10px;font-weight:600;color:var(--brand);margin-top:5px;letter-spacing:.2px}
.call-tab{left:765px;top:0;width:270px;height:42px;background:var(--charcoal);border-radius:0 0 22px 22px;display:flex;align-items:center;padding-left:22px;gap:10px;color:var(--white);font-size:13px;letter-spacing:.4px}
.call-icon{width:26px;height:26px;border-radius:50%;background:#4a4c4f;display:flex;align-items:center;justify-content:center;flex:none}
.nav{top:60px;left:0;width:1200px;height:20px;font-size:13.5px;color:#333}
.nav a{position:absolute;white-space:nowrap}

/* hero */
.hero{left:0;top:93px;width:1200px;height:385px;background:linear-gradient(100deg,#5a4a3a 0%,#8a6c4c 30%,#c89a5c 55%,#e7b36c 75%,#b98552 100%)}
.hero-arrow{top:262px;width:28px;height:46px;background:rgba(60,60,60,.8);display:flex;align-items:center;justify-content:center}
.hero-caption{left:610px;top:184px;width:422px;height:188px;background:rgba(40,40,40,.72);border:2px solid rgba(255,255,255,.15);padding:14px 16px}
.hero-caption h1{font-size:23px;font-weight:400;color:var(--white);padding-bottom:12px;border-bottom:1px solid rgba(255,255,255,.4);white-space:nowrap}
.hero-caption p{font-size:12.5px;line-height:1.6;color:#e5e5e5;margin-top:12px}
.btn-more{display:inline-block;margin-top:14px;background:var(--brand-dark);color:var(--white);font-size:14px;padding:9px 20px;border-radius:2px}

/* intro */
.intro-box{left:165px;top:519px;width:567px;height:226px;border:1px solid var(--line);padding:20px 16px}
.intro-box h2{font-size:24px;font-weight:400;color:var(--ink);padding-bottom:12px;border-bottom:1px solid var(--line);margin-bottom:12px}
.intro-box p{font-size:11.5px;line-height:1.6;color:var(--muted);margin-bottom:6px}
.cta-panel{left:784px;top:519px;width:255px;height:226px;background:var(--panel);border:1px solid var(--line)}
.cta{position:absolute;left:13px;width:229px;height:52px;display:flex;color:var(--white)}
.cta-body{flex:1;padding:8px 14px;font-size:13px;font-weight:600;line-height:1.2}
.cta-body small{display:block;font-size:11px;font-weight:400}
.cta-arrow{width:38px;display:flex;align-items:center;justify-content:center;font-size:15px}
.cta--blue{background:var(--brand-dark)}
.cta--blue .cta-arrow{background:var(--brand)}
.cta--grey{background:#4b4d50}
.cta--grey .cta-arrow{background:#3a3c3e}

.divider{left:0;width:1200px;height:1px;background:var(--line)}
.section-title{left:0;width:1200px;text-align:center;font-size:27px;font-weight:400;color:var(--ink)}
.section-lead{left:170px;width:860px;text-align:center;font-size:11.5px;line-height:1.5;color:#555}

/* experience */
.exp-card{top:915px;width:228px;height:113px;border:1px solid var(--line);padding:14px 12px 0 28px}
.exp-card h3{font-size:14px;font-weight:400;color:var(--ink);margin-bottom:6px;white-space:nowrap}
.exp-card p{font-size:11px;line-height:1.4;color:var(--muted)}
.exp-badge{top:936px;width:70px;height:70px;border-radius:50%;border:3px solid #ddd}

/* who we are */
.who-card{top:1211px;width:275px;height:287px;border:1px solid var(--line);box-shadow:0 1px 3px rgba(0,0,0,.08);padding:10px}
.who-photo{width:100%;height:132px}
.who-card h3{font-size:14px;font-weight:600;text-align:center;color:#333;margin:24px 0 10px}
.who-card p{font-size:11px;line-height:1.55;text-align:center;color:var(--muted)}

/* benefits */
.band{left:0;top:1550px;width:1200px;height:515px;background:linear-gradient(180deg,#3c3e40,#4a4c4d 60%,#3a3b3c)}
.benefit-list{left:186px;top:1589px;width:253px;height:435px;background:var(--white);box-shadow:0 2px 6px rgba(0,0,0,.3)}
.benefit-list h3{background:var(--sky);color:var(--white);font-size:16px;font-weight:600;height:38px;line-height:38px;padding-left:20px}
.benefit-list li{list-style:none;height:34.3px;line-height:34px;padding-left:20px;font-size:13px;color:#444;border-bottom:1px solid #e4e4e4}
.benefit-list li:first-child{background:#f0f0f0}
.benefit-head{left:474px;top:1589px;width:528px;height:46px;background:rgba(30,30,30,.55);color:var(--white);font-size:22px;padding:8px 22px}
.timeline{left:476px;top:1650px;width:1px;height:380px;background:rgba(255,255,255,.3)}
.step{left:490px;width:560px;height:50px}
.step-num{position:absolute;left:0;top:0;width:36px;height:36px;border-radius:50%;border:2px solid rgba(255,255,255,.5);color:#ddd;font-size:14px;display:flex;align-items:center;justify-content:center}
.step h4{position:absolute;left:56px;top:-2px;font-size:15px;font-weight:400;color:var(--white);white-space:nowrap}
.step p{position:absolute;left:56px;top:22px;font-size:10px;color:#c8c8c8;white-space:nowrap}
.step-dot{left:472px;width:9px;height:9px;border-radius:50%;background:#ccc}

/* footer */
.foot-col{top:2096px}
.foot-col h4{font-size:21px;font-weight:400;color:#444;margin-bottom:10px}
.foot-col p,.foot-col li{font-size:11px;line-height:1.6;color:var(--muted);list-style:none}
.foot-col .call-me{display:inline-block;margin-top:6px;font-size:11px;font-weight:600;color:var(--brand)}
.foot-col li.portal{color:var(--brand)}
.foot-brand{left:954px;top:2120px;display:flex;align-items:center;gap:8px}
.foot-brand .brand-mark{width:26px;height:26px}
.foot-brand span{font-size:18px;font-weight:700;color:var(--brand-dark)}
.social{left:954px;top:2172px;display:flex;gap:8px}
.social a{width:24px;height:24px;border-radius:50%;background:#c9c9c9}
.foot-bar{left:0;top:2276px;width:1200px;height:47px;background:var(--footer-bar);color:#bbb;font-size:12px;text-align:center;line-height:47px}
.foot-bar b{color:var(--white);font-weight:400}
</style>
</head>
<body>

<header>
  <div class="abs topline"></div>
  <div class="abs brand">
    <span class="brand-mark"></span>
    <span class="brand-text">
      <span class="brand-name">Talvera</span>
      <span class="brand-tagline">Irrevocably committed to your success</span>
    </span>
  </div>
  <a class="abs call-tab" href="tel:+015550184420">
    <span class="call-icon">
      <svg width="14" height="14" viewBox="0 0 24 24"><path fill="#fff" d="M6.6 10.8a15.1 15.1 0 0 0 6.6 6.6l2.2-2.2c.3-.3.7-.4 1-.2 1.1.4 2.3.6 3.6.6.6 0 1 .4 1 1V20c0 .6-.4 1-1 1C10.6 21 3 13.4 3 4c0-.6.4-1 1-1h3.5c.6 0 1 .4 1 1 0 1.3.2 2.5.6 3.6.1.3 0 .7-.2 1z"/></svg>
    </span>
    CALL US &nbsp;+01 555 018 442
  </a>
  <nav class="abs nav">
    <a href="#" style="left:629px">Home</a>
    <a href="#" style="left:704px">Services</a>
    <a href="#" style="left:795px">About us</a>
    <a href="#" style="left:892px">Gallery</a>
    <a href="#" style="left:977px">Contact Us</a>
  </nav>
</header>

<section>
  <div class="abs hero" role="img" aria-label="Businessman in glasses and tie looking at a tablet, warm blurred city lights behind"></div>
  <div class="abs hero-arrow" style="left:0"><svg width="10" height="16" viewBox="0 0 10 16"><path d="M8 1 2 8l6 7" stroke="#fff" stroke-width="2" fill="none"/></svg></div>
  <div class="abs hero-arrow" style="left:1172px"><svg width="10" height="16" viewBox="0 0 10 16"><path d="m2 1 6 7-6 7" stroke="#fff" stroke-width="2" fill="none"/></svg></div>
  <div class="abs hero-caption">
    <h1>Nam Sagittis Neque Volutpat Arcu</h1>
    <p>Morbi feugiat hendrerit magna. Pellentesque quis dolor felis. Donec suscipit rhoncus nisi, eu scelerisque sem pulvinar et. Quisque nulla lectus, semper at nisl ut, ultricies volutpat nulla.</p>
    <a class="btn-more" href="#">Read More</a>
  </div>
</section>

<section>
  <div class="abs intro-box">
    <h2>Talvera Technical Services</h2>
    <p>Lorem ipsum dolor sit amet, consectetur adipiscing elit. Maecenas facilisis interdum rutrum. Ut dapibus dignissim nibh posuere condimentum. Nam eleifend ullamcorper dui, nec varius eros placerat sodales scelerisque.</p>
    <p>Vestibulum dictum at nunc ac feugiat. Ut eu ipsum minec varius eros placerat in. Maecenas dapibus nunc ac tristique faucibus. Morbi interdum felis est.</p>
    <p>Nullam mattis mi eget orci elementum, eu interdum ligula tincidunt. Curabitur nec pellentesque leotiam bibendum sit amet nisi eget faucibus. Phasellus eleifend dictum dolor</p>
  </div>
  <div class="abs cta-panel">
    <a class="cta cta--blue" href="#" style="top:18px"><div class="cta-body">REQUEST A QUOTE<small>(We'll respond within 24 hrs)</small></div><div class="cta-arrow">»</div></a>
    <a class="cta cta--grey" href="#" style="top:86px"><div class="cta-body">OUR SERVICES<small>(Find out what we do best)</small></div><div class="cta-arrow">»</div></a>
    <a class="cta cta--blue" href="#" style="top:155px"><div class="cta-body">GOT A QUESTION<small>(Check out our FAQ pag)</small></div><div class="cta-arrow">»</div></a>
  </div>
</section>

<div class="abs divider" style="top:774px"></div>

<section>
  <h2 class="abs section-title" style="top:802px">Our experience</h2>
  <p class="abs section-lead" style="top:843px">When it comes to the security of your family online you can't be too careful. We've built our reputation on developing the industry's most comprehensive and technologically advanced network security system to keep your home, and everyone in it, safe online.</p>

  <div class="abs exp-card" style="left:213px"><h3>Praesent Ullamcorper</h3><p>Maecenas et ullamcorper felis.Curabitur in dignissim arcu. In hac platea dictumsttasse .</p></div>
  <div class="abs exp-card" style="left:509px"><h3>Accumsan tellus hendrerit</h3><p>Maecenas et ullamcorper felis.Curabitur in dignissim arcu. In hac platea dictumsttasse .</p></div>
  <div class="abs exp-card" style="left:807px"><h3>Cras accumsan mattis</h3><p>Maecenas et ullamcorper felis.Curabitur in dignissim arcu. In hac platea dictumsttasse .</p></div>

  <div class="abs exp-badge" style="left:162px;background:linear-gradient(135deg,#d9a52c,#4a4a4a)" role="img" aria-label="Technician at work"></div>
  <div class="abs exp-badge" style="left:462px;background:linear-gradient(135deg,#6f8fb0,#2c3e50)" role="img" aria-label="Computer monitor with network diagram"></div>
  <div class="abs exp-badge" style="left:758px;background:linear-gradient(135deg,#e08a2a,#3a5f8a)" role="img" aria-label="Engineer in safety vest"></div>
</section>

<div class="abs divider" style="top:1087px"></div>

<section>
  <h2 class="abs section-title" style="top:1114px">Who we are</h2>
  <p class="abs section-lead" style="top:1155px">When it comes to the security of your family online you can't be too careful. We've built our reputation on developing the industry's most comprehensive and technologically advanced network security system to keep your home, and everyone in it, safe online.</p>

  <article class="abs who-card" style="left:159px">
    <div class="who-photo" style="background:linear-gradient(180deg,#1a5fd0,#0c2f7a)" role="img" aria-label="Silhouettes of business people against a blue technology backdrop"></div>
    <h3>NAM SAGITTIS NEQUE VOLUTPAT</h3>
    <p>In sit amet lacinia lectus. Duis quis mauris eget leo iaculis tincidunt. Vivamus metus ligula, tincidunt sed dictum ut, cursus et augue. Praesent tempor vel nulla tristique gravida. ttis.</p>
  </article>
  <article class="abs who-card" style="left:462px">
    <div class="who-photo" style="background:linear-gradient(135deg,#d8cfc8,#a88b78)" role="img" aria-label="Team of colleagues stacking hands together"></div>
    <h3>NAM SAGITTIS NEQUE VOLUTPAT</h3>
    <p>In sit amet lacinia lectus. Duis quis mauris eget leo iaculis tincidunt. Vivamus metus ligula, tincidunt sed dictum ut, cursus et augue. Praesent tempor vel nulla tristique gravida. ttis.</p>
  </article>
  <article class="abs who-card" style="left:764px">
    <div class="who-photo" style="background:linear-gradient(135deg,#6b5a4a,#3a332c)" role="img" aria-label="Group of people reviewing plans around a table"></div>
    <h3>NAM SAGITTIS NEQUE VOLUTPAT</h3>
    <p>In sit amet lacinia lectus. Duis quis mauris eget leo iaculis tincidunt. Vivamus metus ligula, tincidunt sed dictum ut, cursus et augue. Praesent tempor vel nulla tristique gravida. ttis.</p>
  </article>
</section>

<section>
  <div class="abs band" role="img" aria-label="Dimmed photo of business people with tablets"></div>
  <div class="abs benefit-list">
    <h3>Benefits</h3>
    <ul>
      <li>Sed ut perspiciatis</li><li>unde omnis iste</li><li>natus error sit voluptatem</li><li>accusantium doloremque</li><li>laudantium</li><li>totam rem aperiam</li><li>eaque ipsa quae ab illo</li><li>nventore veritatis et</li><li>quasi architecto beatae</li><li>vitae dicta sunt explicabo.</li><li>Nemo enim ipsam</li>
    </ul>
  </div>
  <div class="abs benefit-head">Benefits of Maintaining Your System</div>
  <div class="abs timeline"></div>

  <div class="abs step-dot" style="top:1655px"></div>
  <div class="abs step" style="top:1650px"><span class="step-num">1</span><h4>Morbi feugiat hendrerit magna. Pellentesque quis dolor</h4><p>In eget sem massa. Donec sit amet nunc sit amet nunc sollicitudin porttitor. Pellentesque in</p></div>
  <div class="abs step-dot" style="top:1690px"></div>
  <div class="abs step" style="top:1718px"><span class="step-num">2</span><h4>Business development platform</h4><p>In eget sem massa. Donec sit amet nunc sit amet nunc sollicitudin porttitor. Pellentesque in tristique</p></div>
  <div class="abs step-dot" style="top:1758px"></div>
  <div class="abs step" style="top:1785px"><span class="step-num">3</span><h4>Main features developed</h4><p>In eget sem massa. Donec sit amet nunc sit amet nunc sollicitudin porttitor. Pellentesque in tristique</p></div>
  <div class="abs step-dot" style="top:1826px"></div>
  <div class="abs step" style="top:1853px"><span class="step-num">5</span><h4>Technological structure supported</h4><p>In eget sem massa. Donec sit amet nunc sit amet nunc sollicitudin porttitor. Pellentesque in tristique</p></div>
  <div class="abs step-dot" style="top:1894px"></div>
  <div class="abs step" style="top:1921px"><span class="step-num">6</span><h4>Sed lacinia magna risus</h4><p>In eget sem massa. Donec sit amet nunc sit amet nunc sollicitudin porttitor. Pellentesque in tristique</p></div>
  <div class="abs step-dot" style="top:1962px"></div>
  <div class="abs step" style="top:1989px"><span class="step-num">7</span><h4>Etiam bibendum sit amet nisi</h4><p>In eget sem massa. Donec sit amet nunc sit amet nunc sollicitudin porttitor. Pellentesque in tristique</p></div>
</section>

<footer>
  <div class="abs foot-col" style="left:159px;width:200px">
    <h4>About Us</h4>
    <p>Duis magna arcu, cursus eu ultrices tincidunt in lectus. In hac habitasse platea dictumst. Vestibulum in est vulputate, imperdiet lorem id, ornare lorem. In bibendum lorem pulvinar congue mollis id quis orci.</p>
  </div>
  <div class="abs foot-col" style="left:426px;width:160px">
    <h4>Main Menu</h4>
    <ul>
      <li><a href="#">Home</a></li><li><a href="#">Services</a></li><li><a href="#">About us</a></li><li><a href="#">Gallery</a></li><li><a href="#">Contact Us</a></li>
      <li class="portal"><a href="#">Customer Login</a></li><li class="portal"><a href="#">Client Portals</a></li>
    </ul>
  </div>
  <div class="abs foot-col" style="left:625px;width:190px">
    <h4>Contact Us</h4>
    <p>Duis magna arcu, cursus eu ultrices tincidunt in lectus. In hac habitasse platea dictumst. Vestibulum in est vulputate, imperdiet lorem id.</p>
    <a class="call-me" href="tel:+015550184420">Call me back »</a>
  </div>
  <div class="abs foot-brand"><span class="brand-mark"></span><span>Talvera</span></div>
  <nav class="abs social" aria-label="Social media">
    <a href="#" aria-label="Social media link 1"></a>
    <a href="#" aria-label="Social media link 2"></a>
    <a href="#" aria-label="Social media link 3"></a>
    <a href="#" aria-label="Social media link 4"></a>
  </nav>
  <div class="abs foot-bar">©2015 <b>Talvera Technical Services</b>, a trade name of Dresgan enterprises llc. All rights reserved.</div>
</footer>

</body>
</html>
```